Corvane Holdings needs a business card

I would like the card to be simple but modern and elegant.
I like black and white.
or black and gold.
we are a private finance lender and also are involved in property and property developments.

please look at the business card photos i provided i would like C.H only one one side and all the other details on the other side use fonts that tie in with my theme.

Industry/Entity Type

Finance

Contact Information for Business Card

Corvane Holdings (C.H) Elliot Marbury M: 0413586102 E: elliotmar@examplemail.net

Font styles to use
Other font styles liked:
• Use fonts that would reflect our business

Colors
000000
ffffff

Requirements
Must have
• one side of details
• other side has either C.H or Corvane Holdings like in the photos provided

```html
<!DOCTYPE html>
<html lang="en">
<head>
<meta charset="utf-8">
<title>Corvane Holdings – Business Card</title>
<link href="https://fonts.googleapis.com/css2?family=Open+Sans:wght@400;600;700;800&display=swap" rel="stylesheet">
<style>
  :root {
    --backdrop: #2e2926;
    --card: #17181a;
    --card-edge: #0e0f10;
    --ink: #f4f4f4;
    --ink-soft: #d9d9d9;
    --silver: #a7a9ab;
    --divider: rgba(255,255,255,0.55);
  }
  * { margin: 0; padding: 0; box-sizing: border-box; }
  html, body {
    width: 1200px; height: 769px; overflow: hidden;
    background: var(--backdrop);
    font-family: "Open Sans", Arial, sans-serif;
  }
  .canvas {
    position: relative; width: 1200px; height: 769px;
    display: flex; align-items: center; justify-content: center; gap: 56px;
  }
  .card {
    position: relative; width: 504px; height: 288px;
    background: var(--card);
    border: 1px solid var(--card-edge);
    box-shadow: 0 18px 40px rgba(0,0,0,0.45);
  }
  /* Details side */
  .card--details { display: flex; align-items: center; }
  .monogram {
    width: 218px; text-align: right; padding-right: 26px;
    font-weight: 800; font-size: 54px; letter-spacing: 1px;
    color: var(--ink);
  }
  .divider {
    width: 1px; height: 132px; background: var(--divider);
  }
  .details { padding-left: 28px; color: var(--ink-soft); }
  .details__name {
    font-weight: 600; font-size: 17px; color: var(--ink);
    margin-bottom: 8px;
  }
  .details__row {
    display: flex; align-items: center; gap: 9px;
    font-size: 13.5px; line-height: 20px;
  }
  .details__row svg { width: 13px; height: 13px; flex: none; }
  /* Brand side */
  .card--brand { display: flex; align-items: center; justify-content: center; }
  .brand-name {
    font-weight: 800; font-size: 31px; letter-spacing: 1.5px;
    color: var(--silver); text-transform: uppercase; text-align: center;
    line-height: 1.1;
  }
</style>
</head>
<body>
  <main class="canvas">
    <section class="card card--details" aria-label="Contact side">
      <div class="monogram">C.H</div>
      <div class="divider"></div>
      <div class="details">
        <p class="details__name">Elliot Marbury</p>
        <p class="details__row">
          <svg viewBox="0 0 13 13" aria-hidden="true"><rect x="3" y="0.8" width="7" height="11.4" rx="1.2" fill="none" stroke="#f4f4f4" stroke-width="1.3"/><circle cx="6.5" cy="10.2" r="0.7" fill="#f4f4f4"/></svg>
          0413586102
        </p>
        <p class="details__row">
          <svg viewBox="0 0 13 13" aria-hidden="true"><rect x="0.8" y="2.5" width="11.4" height="8" fill="#f4f4f4"/><path d="M0.8 2.5 L6.5 7 L12.2 2.5" fill="none" stroke="#17181a" stroke-width="1.2"/></svg>
          elliotmar@examplemail.net
        </p>
        <p class="details__row">
          <svg viewBox="0 0 13 13" aria-hidden="true"><circle cx="6.5" cy="6.5" r="5.7" fill="#f4f4f4"/><path d="M6.5 0.8 V12.2 M0.8 6.5 H12.2" stroke="#17181a" stroke-width="1"/><ellipse cx="6.5" cy="6.5" rx="2.6" ry="5.7" fill="none" stroke="#17181a" stroke-width="1"/></svg>
          www.corvaneholdings.com
        </p>
      </div>
    </section>

    <section class="card card--brand" aria-label="Brand side">
      <p class="brand-name">Corvane<br>Holdings (C.H)</p>
    </section>
  </main>
</body>
</html>
```